Webdesign für Vermietung eines Ferienhauses auf der Insel Usedom
Zielgruppe
Vermietung eines Ferienhauses auf der Insel Usedom
ZG: Urlauber im gehobenem Preissegment, die Luxus schätzen und urlauben wollen
Aufgabenstellung
- IN ADOBE PHOTOSHOP
- Bilder können hier entnommen werden: https://www.quartiro-net.example/ob-link-ansicht-reserve/index.php?portal=48127&unit=39502/index.html
- gern können Sie auch Stock-Bilder verwenden
- Der Buchungskalender /die Verfügbarkeit der freien Zeiträume soll präsent im oberen Bereich der Seite stehen
- Lumivo-Bewertungsbutton
- Es gibt kein Logo - bitte den Namenszug 'KIEFERNVILLA*****HOLMSTEDE' nutzen

```html
<!DOCTYPE html>
<html lang="de">
<head>
<meta charset="utf-8">
<title>Kiefernvilla Holmstede – Webdesign</title>
<link rel="stylesheet" href="https://fonts.googleapis.com/css2?family=Domine:wght@600;700&family=Raleway:wght@400;500;600;700&display=swap">
<style>
  :root{
    --stage:#e0e6f2;
    --ink:#0e0e0e;
    --panel:rgba(70,69,66,.93);
    --panel-solid:#4a4946;
    --sand:#f1eee9;
    --white:#ffffff;
    --text:#2a2a2a;
    --teal:#4f6a6b;
    --line:#d9d6d1;
    --serif:'Domine', Georgia, serif;
    --sans:'Raleway', Arial, sans-serif;
  }
  *{box-sizing:border-box;margin:0;padding:0}
  html,body{width:1200px;height:2181px;overflow:hidden}
  body{background:var(--stage);font-family:var(--sans);color:var(--text);position:relative}
  .screen{position:absolute;background:var(--white);overflow:hidden}
  .screen-desktop{left:138px;top:75px;width:691px;height:1822px;border-radius:14px;box-shadow:0 10px 30px rgba(40,50,80,.12)}
  .screen-mobile{left:891px;top:75px;width:170px;height:1967px;border-radius:8px;box-shadow:0 10px 30px rgba(40,50,80,.12)}
  .abs{position:absolute}
  .band{position:absolute;left:0;right:0}
  .ink{background:var(--ink)}
  .sand{background:var(--sand)}
  .photo{position:absolute}

  /* wordmark: one line, one weight, one colour */
  .wordmark{position:absolute;color:var(--white);font-family:var(--sans);font-weight:600;letter-spacing:.06em;white-space:nowrap;line-height:1}

  .nav{position:absolute;display:flex;font-size:8.4px;letter-spacing:.06em;color:#333}
  .badge{position:absolute;border:1.4px solid #9a9a9a;border-radius:3px;background:#fff}

  .form-title{position:absolute;color:#fff;font-weight:600}
  .field{position:absolute;background:#fff;display:flex;align-items:center}
  .field .ico{height:100%;background:#e9e9ec;display:flex;align-items:center;justify-content:center}
  .btn{position:absolute;background:var(--teal);color:#fff;font-weight:600;display:flex;align-items:center;justify-content:center;letter-spacing:.03em}
  .divider{position:absolute;height:1px;background:rgba(255,255,255,.4)}
  .divider span{position:absolute;left:50%;top:50%;transform:translate(-50%,-50%);background:var(--panel-solid);color:rgba(255,255,255,.7);letter-spacing:.2em;padding:0 6px}
  .review-text{position:absolute;color:#fff;line-height:1.05}
  .review-btn{position:absolute;background:#fff;display:flex;flex-direction:column;align-items:center;justify-content:center;border-radius:1px}
  .review-btn .rv-name{font-weight:600;color:#4a4a4a}
  .review-btn .rv-sub{color:#777}

  .feature{position:absolute;transform:translateX(-50%);text-align:center;color:#666;line-height:1.45;white-space:nowrap}
  .feature svg{display:block;margin:0 auto;color:#333}

  .eyebrow{position:absolute;display:flex;align-items:center;font-weight:700;letter-spacing:.1em;color:#2a2a2a;text-transform:uppercase;white-space:nowrap}
  .eyebrow::before{content:"";display:block;background:#2a2a2a;height:1px;width:var(--rule-w,30px)}
  .heading{position:absolute;font-family:var(--serif);font-weight:600;color:#1b1b1b;line-height:1;white-space:nowrap}
  .copy{position:absolute;color:#3c3c3c}

  .tile{position:absolute}
  .dots{position:absolute;display:flex}
  .dots i{display:block;border-radius:50%;border:1px solid #777}
  .dots i.on{background:#222;border-color:#222}

  .q{position:absolute;font-weight:700;letter-spacing:.12em;color:#222;text-transform:uppercase;white-space:nowrap}
  .rule{position:absolute;height:1px;background:var(--line)}
  .label-muted{position:absolute;font-weight:700;letter-spacing:.12em;color:#8a8a8a;text-transform:uppercase;white-space:nowrap}

  .map{position:absolute;left:0;right:0;background:linear-gradient(135deg,#b3b3b4 0%,#a5a5a6 45%,#b8b8b9 70%,#9b9b9c 100%)}
  .pin{position:absolute}

  .footer-text{position:absolute;color:#cfcfcf}
  .footer-nav{position:absolute;display:flex;color:#eaeaea;white-space:nowrap}
  .footer-line{position:absolute;height:1px;background:#555}
</style>
</head>
<body>

<svg width="0" height="0" style="position:absolute" aria-hidden="true">
  <defs>
    <symbol id="i-house" viewBox="0 0 24 24"><path d="M12 3 1.5 12h3v9h6v-6h3v6h6v-9h3z" fill="currentColor"/></symbol>
    <symbol id="i-people" viewBox="0 0 24 24"><circle cx="7" cy="4" r="2.3" fill="currentColor"/><circle cx="17" cy="4" r="2.3" fill="currentColor"/><path d="M4.5 8h5v7H8.5v7h-3v-7H4.5z" fill="currentColor"/><path d="M17 8l3.5 8h-2v6h-3v-6h-2z" fill="currentColor"/></symbol>
    <symbol id="i-beach" viewBox="0 0 24 24"><path d="M3 10c2-5 8-7 13-5l-3 2.5 5 2-3 1.5C12 9 7 9 3 10z" fill="currentColor"/><path d="M11 8.5 14 21" stroke="currentColor" stroke-width="2"/><path d="M6 21h14" stroke="currentColor" stroke-width="2"/></symbol>
    <symbol id="i-fire" viewBox="0 0 24 24"><rect x="2" y="4" width="20" height="4" fill="currentColor"/><path d="M3 8h18v13h-4v-7H7v7H3z" fill="currentColor"/><circle cx="17" cy="15" r="4" fill="none" stroke="currentColor" stroke-width="2"/></symbol>
    <symbol id="i-pool" viewBox="0 0 24 24"><path d="M7 3v12M7 4h8M7 9h8M15 3v12" stroke="currentColor" stroke-width="2" fill="none"/><path d="M2 17c2.5-2 4.5 2 7 0s4.5 2 7 0 4.5 2 6 0M2 21c2.5-2 4.5 2 7 0s4.5 2 7 0 4.5 2 6 0" stroke="currentColor" stroke-width="1.8" fill="none"/></symbol>
    <symbol id="i-list" viewBox="0 0 24 24"><rect x="2" y="4" width="3" height="3" fill="currentColor"/><rect x="2" y="10.5" width="3" height="3" fill="currentColor"/><rect x="2" y="17" width="3" height="3" fill="currentColor"/><rect x="8" y="4.5" width="14" height="2" fill="currentColor"/><rect x="8" y="11" width="14" height="2" fill="currentColor"/><rect x="8" y="17.5" width="14" height="2" fill="currentColor"/></symbol>
    <symbol id="i-cal" viewBox="0 0 24 24"><rect x="3" y="5" width="18" height="16" rx="2" fill="none" stroke="currentColor" stroke-width="2"/><path d="M3 10h18M8 3v4M16 3v4" stroke="currentColor" stroke-width="2"/></symbol>
    <symbol id="i-guests" viewBox="0 0 24 24"><circle cx="9" cy="8" r="3.5" fill="none" stroke="currentColor" stroke-width="2"/><path d="M2 20c0-4 3-6 7-6s7 2 7 6" fill="none" stroke="currentColor" stroke-width="2"/><path d="M16 5a3 3 0 0 1 0 6M18 14c2 1 4 3 4 6" fill="none" stroke="currentColor" stroke-width="2"/></symbol>
    <symbol id="i-pin" viewBox="0 0 24 36"><circle cx="12" cy="10" r="9" fill="#111"/><path d="M11 18h2l-1 16z" fill="#111"/></symbol>
  </defs>
</svg>

<!-- ================= DESKTOP ================= -->
<main class="screen screen-desktop">

  <header class="site-header">
    <div class="band" style="top:0;height:56px;background:#fff"></div>
    <div class="abs ink" style="left:0;top:0;width:163px;height:56px"></div>
    <p class="wordmark" style="left:0;width:163px;top:24px;text-align:center;font-size:8.6px">KIEFERNVILLA HOLMSTEDE</p>
    <nav class="nav" style="left:194px;top:24px;gap:19px">
      <span>Das 5* Strandhaus</span><span>Verfügbarkeit</span><span>Die Räumlichkeiten</span><span>Lage</span><span>Kontakt</span>
    </nav>
    <div class="badge" style="left:599px;top:15px;width:56px;height:26px"></div>
  </header>

  <section class="hero">
    <div class="photo" role="img" aria-label="Reetgedecktes Ferienhaus mit Terrasse, Rasen und sprudelndem Whirlpool im Vordergrund"
      style="left:0;top:56px;width:691px;height:278px;background:linear-gradient(160deg,#3f5a34 0%,#6f8a55 25%,#c9c6b8 45%,#8f8d85 65%,#5e5c57 85%,#a9a8a2 100%)"></div>
    <div class="abs" style="left:402px;top:56px;width:289px;height:278px;background:var(--panel)"></div>
    <h2 class="form-title" style="left:465px;top:134px;font-size:11.5px">Verfügbarkeit prüfen</h2>
    <div class="field" style="left:465px;top:157px;width:76px;height:18px"><span class="ico" style="width:16px;color:#666"><svg width="8" height="8"><use href="#i-cal"/></svg></span></div>
    <div class="field" style="left:552px;top:157px;width:76px;height:18px"><span class="ico" style="width:16px;color:#666"><svg width="8" height="8"><use href="#i-cal"/></svg></span></div>
    <div class="field" style="left:465px;top:185px;width:76px;height:18px"><span class="ico" style="width:16px;color:#666"><svg width="8" height="8"><use href="#i-guests"/></svg></span></div>
    <div class="btn" style="left:552px;top:185px;width:76px;height:18px;font-size:8px">Jetzt Prüfen</div>
    <div class="divider" style="left:465px;top:218px;width:163px"><span style="font-size:6px">ODER</span></div>
    <p class="review-text" style="left:465px;top:236px;font-size:7.5px">Sehen Sie, was andere<br>Gäste sagen</p>
    <div class="review-btn" style="left:567px;top:233px;width:61px;height:25px">
      <span class="rv-name" style="font-size:11px">Lumivo</span>
      <span class="rv-sub" style="font-size:4.5px">Rezension</span>
    </div>
  </section>

  <section class="features">
    <div class="band sand" style="top:334px;height:71px"></div>
    <div class="feature" style="left:91px;top:350px;font-size:6.2px"><svg width="14" height="14" style="margin-bottom:4px"><use href="#i-house"/></svg>145 qm Wohnfläche<br>700qm Grundstück</div>
    <div class="feature" style="left:185px;top:350px;font-size:6.2px"><svg width="14" height="14" style="margin-bottom:4px"><use href="#i-people"/></svg>Platz für bis<br>zu 7 Personen</div>
    <div class="feature" style="left:276px;top:350px;font-size:6.2px"><svg width="14" height="14" style="margin-bottom:4px"><use href="#i-beach"/></svg>Nur 5 Gehminuten<br>zum Strand</div>
    <div class="feature" style="left:379px;top:350px;font-size:6.2px"><svg width="14" height="14" style="margin-bottom:4px"><use href="#i-fire"/></svg>Kamin für<br>gemütliche Abende</div>
    <div class="feature" style="left:490px;top:350px;font-size:6.2px"><svg width="14" height="14" style="margin-bottom:4px"><use href="#i-pool"/></svg>Eigene Sauna und<br>ganzjährlicher Whirlpool</div>
    <div class="feature" style="left:609px;top:350px;font-size:6.2px"><svg width="14" height="14" style="margin-bottom:4px"><use href="#i-list"/></svg>Entdecken Sie<br>alle Vorteile -&gt;</div>
  </section>

  <section class="intro">
    <div class="band" style="top:405px;height:388px;background:linear-gradient(#f6f6f6,#fff 30%,#fff 70%,#f9f9f9)"></div>
    <div class="photo" role="img" aria-label="Garten mit Gartenhaus, Kiefern und blühendem Strauch" style="left:462px;top:506px;width:155px;height:89px;background:linear-gradient(135deg,#3d4a30,#6b7a58 50%,#8d8ab0)"></div>
    <div class="photo" role="img" aria-label="Weißes Haus mit Reetdach vor blauem Himmel" style="left:378px;top:547px;width:169px;height:113px;background:linear-gradient(160deg,#5d86c2 0%,#9bb6d8 35%,#e9e6df 55%,#5e6b45 85%)"></div>
    <div class="photo" role="img" aria-label="Terrasse mit Liegestühlen und Blick ins Grüne" style="left:547px;top:591px;width:86px;height:101px;background:linear-gradient(160deg,#d8dcd6,#9aa789 50%,#b58a5c)"></div>
    <div class="photo" role="img" aria-label="Holzterrasse mit Gartenmöbeln und türkisen Kissen" style="left:482px;top:641px;width:65px;height:51px;background:linear-gradient(160deg,#c6a57b,#f0ede6 50%,#2a9aa0)"></div>
    <p class="eyebrow" style="left:58px;top:552px;font-size:6.5px;gap:8px;--rule-w:32px">Herzlich Willkommen in Ihrem</p>
    <h1 class="heading" style="left:58px;top:563px;font-size:29px">5 Sterne Strandhaus</h1>
    <p class="copy" style="left:58px;top:601px;width:272px;font-size:7.6px;line-height:1.85">Dieses exklusive, 2017 erbaute Strandhaus mit ca. 145 m² Wohnfläche und einem Grundstück von ca. 700 m² befindet sich ca. 5 Gehminuten vom Strand entfernt.</p>
    <div class="btn" style="left:58px;top:652px;width:95px;height:23px;font-size:8.5px">Mehr Erfahren</div>
  </section>

  <section class="gallery">
    <div class="band sand" style="top:793px;height:371px"></div>
    <p class="eyebrow" style="left:39px;top:841px;font-size:6.5px;gap:8px;--rule-w:32px">Entdecken Sie das</p>
    <h2 class="heading" style="left:39px;top:852px;font-size:21px">Strandhaus Holmstede</h2>
    <p class="abs" style="right:38px;top:842px;font-size:6.5px;font-weight:700;letter-spacing:.1em">ZUR GALLERIE</p>
    <div class="tile" role="img" aria-label="Moderne Küche mit Espressomaschine und Tassen" style="left:39px;top:891px;width:151px;height:99px;background:linear-gradient(150deg,#7d8078,#4a4b47 45%,#a9a59c)"></div>
    <div class="tile" role="img" aria-label="Gedeckter Esstisch im hellen Wohnbereich" style="left:194px;top:891px;width:151px;height:99px;background:linear-gradient(150deg,#c8cbb9,#8e8c7f 45%,#e2ddd2)"></div>
    <div class="tile" role="img" aria-label="Wohnzimmer mit Sofa und Kronleuchter" style="left:349px;top:891px;width:151px;height:99px;background:linear-gradient(150deg,#e6e4de,#bfbcb4 50%,#5d5d5b)"></div>
    <div class="tile" role="img" aria-label="Offener Wohn- und Essbereich mit Kamin" style="left:503px;top:891px;width:150px;height:99px;background:linear-gradient(150deg,#d6dcd2,#a7a59a 50%,#eeebe4)"></div>
    <div class="tile" role="img" aria-label="Schlafzimmer mit gestreifter Bettwäsche" style="left:39px;top:999px;width:151px;height:100px;background:linear-gradient(150deg,#e5e2dc,#cbb899 55%,#8b6e4d)"></div>
    <div class="tile" role="img" aria-label="Schlafzimmer mit Holzbett und bunten Kissen" style="left:194px;top:999px;width:151px;height:100px;background:linear-gradient(150deg,#dcd8d0,#b59882 50%,#6a4d3b)"></div>
    <div class="tile" role="img" aria-label="Leuchte mit bunten Glaskugeln" style="left:349px;top:999px;width:151px;height:100px;background:radial-gradient(circle at 50% 45%,#f6e3a0,#c4772c 35%,#5a3b20 75%)"></div>
    <div class="tile" role="img" aria-label="Essstuhl und dekoratives Kissen im Detail" style="left:503px;top:999px;width:150px;height:100px;background:linear-gradient(150deg,#5b5a56,#8a8983 50%,#e4e4e1)"></div>
    <div class="dots" style="left:323px;top:1112px;gap:5px"><i class="on" style="width:5px;height:5px"></i><i style="width:5px;height:5px"></i><i style="width:5px;height:5px"></i><i style="width:5px;height:5px"></i><i style="width:5px;height:5px"></i></div>
  </section>

  <section class="faq">
    <p class="eyebrow" style="left:111px;top:1206px;font-size:6.5px;gap:8px;--rule-w:32px">Häufige Fragen</p>
    <h2 class="heading" style="left:111px;top:1217px;font-size:21px">Schnell beantwortet</h2>
    <p class="q" style="left:111px;top:1266px;font-size:6.4px">Wann ist Check-In? ⌄</p>
    <p class="copy" style="left:111px;top:1284px;width:322px;font-size:7px;line-height:1.85">Lorem ipsum dolor sit amet, consetetur sadipscing elitr, sed diam nonumy eirmod tempor invidunt ut labore et dolore magna aliquyam erat, sed diam voluptua. At vero eos et accusam et justo duo dolores et ea rebum. Stet clita kasd gubergren.</p>
    <div class="rule" style="left:111px;top:1337px;width:322px"></div>
    <p class="q" style="left:111px;top:1353px;font-size:6.4px">Ist eine Langzeit Miete möglich? ›</p>
    <div class="rule" style="left:111px;top:1376px;width:322px"></div>
    <p class="q" style="left:111px;top:1391px;font-size:6.4px">Gibt es Corona Auflagen? ›</p>
    <p class="label-muted" style="left:495px;top:1266px;font-size:6.4px">Sie haben eine Frage?</p>
    <p class="copy" style="left:495px;top:1282px;width:100px;font-size:7.4px;line-height:1.8">Sollten Sie noch offene Fragen haben, so kontaktieren Sie uns einfach.</p>
    <div class="btn" style="left:495px;top:1344px;width:65px;height:18px;font-size:7.4px;font-weight:500">Frage stellen</div>
  </section>

  <section class="location">
    <div class="map" role="img" aria-label="Karte der Umgebung mit Markierung der Ferienhaus-Lage" style="top:1449px;height:213px"></div>
    <svg class="pin" style="left:506px;top:1548px" width="16" height="24"><use href="#i-pin"/></svg>
  </section>

  <footer class="site-footer">
    <div class="band ink" style="top:1662px;height:160px"></div>
    <p class="wordmark" style="left:39px;top:1716px;font-size:8.6px">KIEFERNVILLA HOLMSTEDE</p>
    <p class="footer-text" style="left:39px;top:1751px;font-size:6.4px;line-height:1.95">Exklusives schilfrohrgedecktes, 2017 erbautes<br>Strandhaus in der 5-Sterne-Haus-Anlage<br>"Dünenwerk Küstenland" in Holmstede.</p>
    <nav class="footer-nav" style="right:39px;top:1712px;gap:13px;font-size:7.4px"><span>Das 5* Strandhaus</span><span>Verfügbarkeit</span><span>Die Räumlichkeiten</span><span>Lage</span><span>Kontakt</span></nav>
    <div class="footer-line" style="left:299px;right:39px;top:1736px"></div>
    <nav class="footer-nav" style="right:39px;top:1750px;gap:13px;font-size:6.4px"><span>Impressum</span><span>Datenschutz</span></nav>
  </footer>
</main>

<!-- ================= MOBILE ================= -->
<main class="screen screen-mobile">

  <header class="site-header">
    <div class="band ink" style="top:0;height:34px"></div>
    <p class="wordmark" style="left:7px;top:14px;font-size:6px">KIEFERNVILLA HOLMSTEDE</p>
    <div class="abs" style="left:136px;top:0;width:34px;height:34px;background:#fff">
      <svg width="34" height="34" aria-label="Menü"><path d="M10 12h15M10 17h15M10 22h15" stroke="#111" stroke-width="1.5"/></svg>
    </div>
  </header>

  <section class="hero">
    <div class="photo" role="img" aria-label="Reetgedecktes Ferienhaus mit Whirlpool im Vordergrund" style="left:0;top:34px;width:170px;height:103px;background:linear-gradient(160deg,#3f5a34 0%,#7a9263 30%,#c9c6b8 55%,#9a978f 80%,#b4b2ac 100%)"></div>
    <div class="band" style="top:137px;height:131px;background:var(--panel-solid)"></div>
    <h2 class="form-title" style="left:8px;top:152px;font-size:7.4px">Verfügbarkeit prüfen</h2>
    <div class="field" style="left:8px;top:169px;width:68px;height:16px"><span class="ico" style="width:13px;color:#666"><svg width="6" height="6"><use href="#i-cal"/></svg></span></div>
    <div class="field" style="left:87px;top:169px;width:68px;height:16px"><span class="ico" style="width:13px;color:#666"><svg width="6" height="6"><use href="#i-cal"/></svg></span></div>
    <div class="field" style="left:8px;top:195px;width:68px;height:16px"><span class="ico" style="width:13px;color:#666"><svg width="6" height="6"><use href="#i-guests"/></svg></span></div>
    <div class="btn" style="left:87px;top:195px;width:68px;height:16px;font-size:6.4px">Jetzt Prüfen</div>
    <div class="divider" style="left:8px;top:224px;width:147px"><span style="font-size:4.5px">ODER</span></div>
    <p class="review-text" style="left:8px;top:237px;font-size:5px">Sehen Sie, was andere<br>Gäste sagen</p>
    <div class="review-btn" style="left:108px;top:234px;width:47px;height:18px">
      <span class="rv-name" style="font-size:8px">Lumivo</span>
      <span class="rv-sub" style="font-size:3.5px">Rezension</span>
    </div>
  </section>

  <section class="features">
    <div class="band sand" style="top:268px;height:201px"></div>
    <div class="feature" style="left:43px;top:284px;font-size:5px"><svg width="11" height="11" style="margin-bottom:4px"><use href="#i-house"/></svg>145 qm Wohnfläche<br>700qm Grundstück</div>
    <div class="feature" style="left:125px;top:284px;font-size:5px"><svg width="11" height="11" style="margin-bottom:4px"><use href="#i-people"/></svg>Platz für bis<br>zu 7 Personen</div>
    <div class="feature" style="left:43px;top:350px;font-size:5px"><svg width="11" height="11" style="margin-bottom:4px"><use href="#i-beach"/></svg>Nur 5 Gehminuten<br>zum Strand</div>
    <div class="feature" style="left:125px;top:350px;font-size:5px"><svg width="11" height="11" style="margin-bottom:4px"><use href="#i-fire"/></svg>Kamin für<br>gemütliche Abende</div>
    <div class="feature" style="left:43px;top:414px;font-size:5px"><svg width="11" height="11" style="margin-bottom:4px"><use href="#i-pool"/></svg>Eigene Sauna und<br>ganzjährlicher Whirlpool</div>
    <div class="feature" style="left:125px;top:414px;font-size:5px"><svg width="11" height="11" style="margin-bottom:4px"><use href="#i-list"/></svg>Entdecken Sie<br>alle Vorteile -&gt;</div>
  </section>

  <section class="intro">
    <div class="band" style="top:469px;height:309px;background:linear-gradient(#f6f6f6,#fff 30%)"></div>
    <div class="photo" role="img" aria-label="Garten mit Kiefern" style="left:59px;top:504px;width:95px;height:50px;background:linear-gradient(135deg,#3d4a30,#6b7a58 50%,#8d8ab0)"></div>
    <div class="photo" role="img" aria-label="Weißes Haus mit Reetdach" style="left:7px;top:530px;width:103px;height:66px;background:linear-gradient(160deg,#5d86c2,#9bb6d8 35%,#e9e6df 55%,#5e6b45 85%)"></div>
    <div class="photo" role="img" aria-label="Terrasse mit Liegestühlen" style="left:110px;top:553px;width:53px;height:66px;background:linear-gradient(160deg,#d8dcd6,#9aa789 50%,#b58a5c)"></div>
    <div class="photo" role="img" aria-label="Holzterrasse mit türkisen Kissen" style="left:70px;top:596px;width:40px;height:23px;background:linear-gradient(160deg,#c6a57b,#f0ede6 50%,#2a9aa0)"></div>
    <p class="eyebrow" style="left:8px;top:642px;font-size:4px;gap:5px;--rule-w:18px">Herzlich Willkommen in Ihrem</p>
    <h1 class="heading" style="left:8px;top:650px;font-size:13.5px">5 Sterne Strandhaus</h1>
    <p class="copy" style="left:8px;top:672px;width:155px;font-size:5.6px;line-height:1.95">Dieses exklusive, 2017 erbaute Strandhaus mit ca. 145 m² Wohnfläche und einem Grundstück von ca. 700 m² befindet sich ca. 5 Gehminuten vom Strand entfernt.</p>
    <div class="btn" style="left:8px;top:728px;width:74px;height:18px;font-size:6.2px">Mehr Erfahren</div>
  </section>

  <section class="gallery">
    <div class="band sand" style="top:778px;height:337px"></div>
    <p class="eyebrow" style="left:8px;top:815px;font-size:4px;gap:5px;--rule-w:18px">Entdecken Sie das</p>
    <h2 class="heading" style="left:8px;top:823px;font-size:12.5px">Strandhaus Holmstede</h2>
    <div class="tile" role="img" aria-label="Küche" style="left:8px;top:845px;width:77px;height:51px;background:linear-gradient(150deg,#7d8078,#4a4b47 45%,#a9a59c)"></div>
    <div class="tile" role="img" aria-label="Esstisch" style="left:87px;top:845px;width:76px;height:51px;background:linear-gradient(150deg,#c8cbb9,#8e8c7f 45%,#e2ddd2)"></div>
    <div class="tile" role="img" aria-label="Schlafzimmer mit gestreifter Bettwäsche" style="left:8px;top:900px;width:77px;height:51px;background:linear-gradient(150deg,#e5e2dc,#cbb899 55%,#8b6e4d)"></div>
    <div class="tile" role="img" aria-label="Schlafzimmer mit Holzbett" style="left:87px;top:900px;width:76px;height:51px;background:linear-gradient(150deg,#dcd8d0,#b59882 50%,#6a4d3b)"></div>
    <div class="tile" role="img" aria-label="Wohnzimmer" style="left:8px;top:955px;width:77px;height:50px;background:linear-gradient(150deg,#e6e4de,#bfbcb4 50%,#5d5d5b)"></div>
    <div class="tile" role="img" aria-label="Wohn- und Essbereich" style="left:87px;top:955px;width:76px;height:50px;background:linear-gradient(150deg,#d6dcd2,#a7a59a 50%,#eeebe4)"></div>
    <div class="tile" role="img" aria-label="Leuchte mit bunten Glaskugeln" style="left:8px;top:1010px;width:77px;height:51px;background:radial-gradient(circle at 50% 45%,#f6e3a0,#c4772c 35%,#5a3b20 75%)"></div>
    <div class="tile" role="img" aria-label="Essstuhl und Kissen" style="left:87px;top:1010px;width:76px;height:51px;background:linear-gradient(150deg,#5b5a56,#8a8983 50%,#e4e4e1)"></div>
    <div class="dots" style="left:66px;top:1077px;gap:4px"><i class="on" style="width:4px;height:4px"></i><i style="width:4px;height:4px"></i><i style="width:4px;height:4px"></i><i style="width:4px;height:4px"></i><i style="width:4px;height:4px"></i></div>
  </section>

  <section class="faq">
    <p class="eyebrow" style="left:8px;top:1147px;font-size:4px;gap:5px;--rule-w:18px">Häufige Fragen</p>
    <h2 class="heading" style="left:8px;top:1155px;font-size:12.5px">Schnell beantwortet</h2>
    <p class="q" style="left:8px;top:1185px;font-size:5px">Wann ist Check-In? ⌄</p>
    <p class="copy" style="left:8px;top:1199px;width:155px;font-size:5.6px;line-height:2.05">Lorem ipsum dolor sit amet, consetetur sadipscing elitr, sed diam nonumy eirmod tempor invidunt ut labore et dolore magna aliquyam erat. At vero eos et accusam et justo duo dolores et ea rebum. Stet clita kasd gubergren.</p>
    <p class="q" style="left:8px;top:1301px;font-size:5px">Ist eine Langzeit Miete möglich? ›</p>
    <div class="rule" style="left:8px;top:1321px;width:155px"></div>
    <p class="q" style="left:8px;top:1335px;font-size:5px">Gibt es Corona Auflagen? ›</p>
    <p class="label-muted" style="left:8px;top:1371px;font-size:5px">Sie haben eine Frage?</p>
    <p class="copy" style="left:8px;top:1382px;width:160px;font-size:5.6px;line-height:2">Sollten Sie noch offene Fragen haben,<br>so kontaktieren Sie uns einfach.</p>
    <div class="btn" style="left:8px;top:1410px;width:59px;height:16px;font-size:6px;font-weight:500">Frage stellen</div>
  </section>

  <section class="location">
    <div class="map" role="img" aria-label="Karte der Umgebung mit Markierung der Ferienhaus-Lage" style="top:1462px;height:194px"></div>
    <svg class="pin" style="left:105px;top:1525px" width="13" height="20"><use href="#i-pin"/></svg>
  </section>

  <footer class="site-footer">
    <div class="band ink" style="top:1656px;height:311px"></div>
    <nav class="abs" style="left:0;right:0;top:1685px;text-align:center;color:#eaeaea;font-size:5.8px;line-height:22.7px">
      Das 5* Strandhaus<br>Verfügbarkeit<br>Die Räumlichkeiten<br>Lage<br>Kontakt
    </nav>
    <div class="footer-line" style="left:8px;right:8px;top:1812px"></div>
    <p class="wordmark" style="left:0;right:0;top:1851px;text-align:center;font-size:7.4px">KIEFERNVILLA HOLMSTEDE</p>
    <p class="footer-text" style="left:0;right:0;top:1883px;text-align:center;font-size:5.2px;line-height:2.1">Exklusives schilfrohrgedecktes, 2017 erbautes<br>Strandhaus in der 5-Sterne-Haus-Anlage<br>"Dünenwerk Küstenland" in Holmstede.</p>
    <nav class="footer-nav" style="left:0;right:0;top:1938px;justify-content:center;gap:10px;font-size:5.2px"><span>Impressum</span><span>Datenschutz</span></nav>
  </footer>
</main>

</body>
</html>
```